Tranquil Pathway Business Card

Logo attached. (will be printing onto thick white/off white textured card)

Double sided business card for two Therapists working at Tranquil Pathway.

Require one design, but with different name and mobile numbers on each card.

Target Market(s)

Medical, Health

Industry/Entity Type

Business

Contact Information for Business Card

Need one business card design, but a separate card for each person - Colin Marchetti and Marieke de Boeckx.

FRONT OF CARD

Logo

Name (Colin Marchetti on one card, Marieke de Boeckx on the other)
Professional Clinical Hypnotherapist

Consulting Rooms (Near Lindqvist Hospital)
482 Brackenfield Road
Dunmore VIC 3987

Colin@TranquilPathway.example.au OR Marieke@TranquilPathway.example.au

Mobile: 0455 872 604 (for Colin) OR
Mobile: 0467 290 518 (for Marieke)

BACK OF CARD

Logo

Website: www.TranquilPathway.example.au

Phone: 1300 958 471

Requirements
Must have
• Text and logo only. No additiional graphics.

```html
<!DOCTYPE html>
<html lang="en">
<head>
<meta charset="utf-8">
<title>Tranquil Pathway Business Card</title>
<link rel="stylesheet" href="https://fonts.googleapis.com/css2?family=Open+Sans:wght@400;600;700&display=swap">
<style>
  :root {
    --backdrop: #000000;
    --card-white: #ffffff;
    --navy: #222c62;
    --navy-deep: #1c2458;
    --text-grey: #3d3d3d;
    --ring-grey: #5e5e5e;
    --on-navy: #ffffff;
  }
  html, body {
    margin: 0;
    padding: 0;
    width: 1200px;
    height: 900px;
    overflow: hidden;
    background: var(--backdrop);
    font-family: "Open Sans", Arial, sans-serif;
  }
  .canvas {
    position: relative;
    width: 1200px;
    height: 900px;
  }
  .card {
    position: absolute;
    top: 275px;
    width: 477px;
    height: 293px;
    box-sizing: border-box;
  }
  .card-front {
    left: 116px;
    background: var(--card-white);
    border-radius: 0 48px 0 48px;
  }
  .card-back {
    left: 622px;
    background: var(--navy);
    border-radius: 48px 0 48px 0;
  }
  .front-block {
    position: absolute;
    right: 20px;
    text-align: right;
    color: var(--text-grey);
  }
  .person-name {
    top: 44px;
    margin: 0;
    font-size: 17.5px;
    font-weight: 700;
    color: var(--navy-deep);
    letter-spacing: 0.2px;
  }
  .person-role {
    top: 70px;
    margin: 0;
    font-size: 11px;
  }
  .address {
    top: 168px;
    margin: 0;
    font-style: normal;
    font-size: 13px;
    line-height: 14.5px;
  }
  .contact-line {
    position: absolute;
    right: 20px;
    display: flex;
    align-items: center;
    gap: 8px;
    font-size: 13px;
    color: var(--text-grey);
  }
  .contact-mobile { top: 228px; }
  .contact-email { top: 246px; }
  .contact-line svg { width: 10px; height: 10px; fill: var(--navy); }
  .front-brand {
    position: absolute;
    left: 25px;
    top: 103px;
    display: flex;
    align-items: center;
    gap: 14px;
  }
  .brand-dot {
    width: 60px;
    height: 60px;
    border-radius: 50%;
    background: var(--navy);
    border: 5px solid var(--ring-grey);
  }
  .brand-name {
    font-size: 20px;
    font-weight: 700;
    color: var(--navy-deep);
    line-height: 22px;
    text-transform: uppercase;
  }
  .back-brand {
    position: absolute;
    left: 143px;
    top: 56px;
    width: 158px;
    height: 158px;
    border-radius: 50%;
    border: 8px solid var(--on-navy);
    box-sizing: border-box;
    display: flex;
    align-items: center;
    justify-content: center;
    text-align: center;
  }
  .back-brand .brand-name {
    color: var(--on-navy);
    font-size: 19px;
  }
  .back-phone {
    position: absolute;
    left: 336px;
    top: 122px;
    display: flex;
    align-items: center;
    gap: 4px;
    font-size: 13px;
    font-weight: 600;
    color: var(--on-navy);
  }
  .back-phone svg { width: 11px; height: 11px; fill: var(--on-navy); }
  .website {
    position: absolute;
    left: 0;
    right: 0;
    top: 249px;
    padding-left: 10px;
    text-align: center;
    font-size: 13px;
    font-weight: 600;
    color: var(--on-navy);
  }
</style>
</head>
<body>
<div class="canvas">
  <section class="card card-front" aria-label="Front of card">
    <div class="front-brand">
      <div class="brand-dot"></div>
      <div class="brand-name">Tranquil<br>Pathway</div>
    </div>
    <h1 class="front-block person-name">COLIN MARCHETTI</h1>
    <p class="front-block person-role">Professional Clinical Hypnotherapist</p>
    <address class="front-block address">Consulting Rooms<br>482 Brackenfield Road<br>Dunmore VIC 3987</address>
    <div class="contact-line contact-mobile">
      <span>0455 872 604</span>
      <svg viewBox="0 0 24 24" aria-hidden="true"><path d="M2 8c0-3 5-5 10-5s10 2 10 5v2h-5V8c-1-1-3-1-5-1s-4 0-5 1v2H2zM6 11h12l3 9H3z"/></svg>
    </div>
    <div class="contact-line contact-email">
      <span>Colin@TranquilPathway.example.au</span>
      <svg viewBox="0 0 24 24" aria-hidden="true"><path d="M2 5h20v14H2zM3 6l9 7 9-7v1l-9 7-9-7z"/></svg>
    </div>
  </section>

  <section class="card card-back" aria-label="Back of card">
    <div class="back-brand">
      <div class="brand-name">Tranquil<br>Pathway</div>
    </div>
    <div class="back-phone">
      <svg viewBox="0 0 24 24" aria-hidden="true"><path d="M6.6 10.8a15 15 0 0 0 6.6 6.6l2.2-2.2c.3-.3.7-.4 1-.2 1.1.4 2.3.6 3.6.6.6 0 1 .4 1 1V20c0 .6-.4 1-1 1A17 17 0 0 1 3 4c0-.6.4-1 1-1h3.5c.6 0 1 .4 1 1 0 1.3.2 2.5.6 3.6.1.3 0 .7-.2 1z"/></svg>
      <span>1300 958 471</span>
    </div>
    <div class="website">www.TranquilPathway.example.au</div>
  </section>
</div>
</body>
</html>
```